Web Design Project

we are launching a second screen solutions distribution company for Mexico and Latam, where broadcasters are starting getting acquainted with the concept and reach of these technology. we need a ludic simple and friendly website design for them to navigate on our business proposal. Our entry level product is a educational course about second screen and its immediate benefits to the broadcasting industry.
If you have any question please write me to tomas.dualview@mailbox-example.net
please refer to www.vorpamedia.example
Vorpamedia as our key partner will provide images and at some point we would need to be the spanish speaking mirrored page for Vorpa but I like to give it a boost
Please consider a strategic space to locate VorpaMedia logo as key partner within your design proposal
Target Market(s)
Broadcast Business executives, TV Stations, Radio Stations, sponsors and media agencies.
Industry/Entity Type
Business
Requirements
Must have
- Would like it simple, intuitive, friendly to the eye and mind
one landing page with links to 3 to 5 sections
Nice to have
- some multi screen images would be helpful including TV, Phone, lap top, tablet, etc.

```html
<!DOCTYPE html>
<html lang="en">
<head>
<meta charset="utf-8">
<title>Lumora — second screen solutions</title>
<link rel="stylesheet" href="https://fonts.googleapis.com/css2?family=Montserrat:wght@400;500&display=swap">
<style>
  :root {
    --accent-orange: #f26a0f;
    --nav-grey: #a9a9a9;
    --wordmark-grey: #5f5f5f;
    --page-white: #ffffff;
    --hero-dark: #2a140c;
    --hero-mid: #6b4630;
    --hero-light: #9c7a5c;
    --chevron: rgba(210, 205, 200, 0.75);
  }
  * { margin: 0; padding: 0; box-sizing: border-box; }
  html, body {
    width: 1200px;
    height: 579px;
    overflow: hidden;
    background: var(--page-white);
    font-family: "Montserrat", sans-serif;
  }
  .site {
    position: relative;
    width: 1200px;
    height: 579px;
  }
  .site-header {
    position: absolute;
    top: 0; left: 0;
    width: 1200px;
    height: 85px;
    background: var(--page-white);
  }
  .brand-name {
    position: absolute;
    left: 136px;
    top: 31px;
    font-weight: 500;
    font-size: 17px;
    line-height: 24px;
    letter-spacing: 3px;
    text-transform: uppercase;
    color: var(--wordmark-grey);
  }
  .main-nav {
    position: absolute;
    top: 34px;
    left: 604px;
  }
  .main-nav a {
    position: absolute;
    white-space: nowrap;
    font-size: 14.5px;
    font-weight: 400;
    color: var(--nav-grey);
    text-decoration: none;
  }
  .main-nav .nav-about { left: 0; }
  .main-nav .nav-showcase { left: 111px; }
  .main-nav .nav-quotes { left: 231px; }
  .main-nav .nav-blog { left: 330px; }
  .main-nav .nav-contact { left: 409px; }

  .hero {
    position: absolute;
    top: 85px; left: 0;
    width: 1200px;
    height: 494px;
    overflow: hidden;
  }
  .hero-photo {
    position: absolute;
    inset: 0;
    background:
      radial-gradient(ellipse 70% 80% at 65% 40%, var(--hero-light) 0%, var(--hero-mid) 55%, var(--hero-dark) 100%),
      var(--hero-mid);
  }
  .hero-content {
    position: absolute;
    inset: 0;
    text-align: center;
  }
  .hero-title {
    position: absolute;
    left: 0;
    width: 1200px;
    top: 128px;
    font-weight: 500;
    font-size: 72px;
    line-height: 90px;
    letter-spacing: 14px;
    text-indent: 14px;
    text-transform: uppercase;
    color: var(--page-white);
  }
  .hero-tagline {
    position: absolute;
    left: 0;
    width: 1200px;
    top: 246px;
    font-weight: 500;
    font-size: 16px;
    line-height: 23px;
    color: var(--page-white);
    text-transform: uppercase;
    letter-spacing: 0.3px;
  }
  .scroll-cue {
    position: absolute;
    left: 578px;
    top: 401px;
    width: 45px;
    height: 30px;
  }
</style>
</head>
<body>
<div class="site">
  <header class="site-header">
    <div class="brand-name">Lumora</div>
    <nav class="main-nav">
      <a class="nav-about" href="#about">About us</a>
      <a class="nav-showcase" href="#showcase">Showcase</a>
      <a class="nav-quotes" href="#quotes">Quotes</a>
      <a class="nav-blog" href="#blog">Blog</a>
      <a class="nav-contact" href="#contact">Contact</a>
    </nav>
  </header>

  <section class="hero">
    <div class="hero-photo" role="img" aria-label="Sepia photo of old vintage television sets with antennas stacked in front of a brick wall"></div>
    <div class="hero-content">
      <h1 class="hero-title">Lumora</h1>
      <p class="hero-tagline">New generation in television networking, delivering<br>the absolute best to serve humanity.</p>
      <svg class="scroll-cue" viewBox="0 0 45 30" aria-hidden="true">
        <polyline points="4,6 22.5,24 41,6" fill="none" stroke="var(--chevron)" stroke-width="9"/>
      </svg>
    </div>
  </section>
</div>
</body>
</html>
```